Internet Of Things brochure

Need to create a brochure with a common theme to our website and the last 2 pages of the attached file. All the contect is in the file that I have attached.
website www.norvalegroup.com.au

Industry/Entity Type

Internet

```html
<!DOCTYPE html>
<html lang="en">
<head>
<meta charset="utf-8">
<title>Smart Cities Initiative – Norvale Group</title>
<link href="https://fonts.googleapis.com/css2?family=Exo+2:wght@600;700&family=Source+Sans+3:wght@400;600;700&display=swap" rel="stylesheet">
<style>
  :root {
    --page-bg: #ecedef;
    --navy: #2b4a9a;
    --rule-blue: #2c5aa8;
    --title-band: #35245e;
    --body-text: #333840;
    --footer-bg: #1c1c1e;
    --governance: #29a9e0;
    --economy: #e8224a;
    --mobility: #f2cf14;
    --environment: #3aaa35;
    --people: #d9822b;
    --living: #f08a1a;
  }
  * { box-sizing: border-box; margin: 0; padding: 0; }
  html, body { width: 1200px; height: 1200px; overflow: hidden; background: var(--page-bg); }
  body { font-family: "Source Sans 3", "Helvetica Neue", Arial, sans-serif; position: relative; }

  .flyer {
    position: absolute; left: 144px; top: 20px; width: 912px; height: 1160px;
    background: linear-gradient(180deg, #ffffff 0%, #f3f8fd 60%, #e9f2fb 100%);
    box-shadow: 0 4px 18px rgba(0,0,0,.12);
    overflow: hidden;
  }

  .masthead {
    position: absolute; left: 0; top: 0; width: 912px; height: 118px;
    background: linear-gradient(100deg, #ffffff 0%, #eef5fd 45%, #dfeaf8 100%);
    border-bottom: 5px solid var(--rule-blue);
  }
  .brand {
    position: absolute; left: 90px; top: 36px;
    display: flex; align-items: center; gap: 10px;
  }
  .brand-mark { width: 26px; height: 26px; background: var(--navy); }
  .brand-name { font-size: 34px; font-weight: 700; color: var(--navy); letter-spacing: -.3px; }
  .call {
    position: absolute; right: 41px; top: 44px;
    font-size: 40px; font-weight: 700; color: var(--navy); letter-spacing: -.3px; line-height: 1;
  }

  .hero-photo {
    position: absolute; left: 0; top: 123px; width: 912px; height: 348px;
    background: radial-gradient(ellipse at 55% 45%, #c9dcef 0%, #7f9ab8 45%, #2d3e5a 100%);
  }

  .title-band {
    position: absolute; left: 0; top: 475px; width: 912px; height: 71px;
    background: var(--title-band);
    display: flex; align-items: center; justify-content: center;
  }
  .title-band h1 {
    font-family: "Exo 2", "Trebuchet MS", sans-serif; font-weight: 700;
    font-size: 50px; color: #fff; letter-spacing: .2px;
  }

  .intro {
    position: absolute; left: 35px; top: 556px; width: 836px;
    font-size: 12.8px; line-height: 16px; color: var(--body-text); text-align: justify;
  }

  .pillars {
    position: absolute; left: 44px; top: 754px; width: 818px; height: 312px;
    border: 2px solid var(--rule-blue);
    display: grid; grid-template-columns: repeat(3, 1fr); grid-template-rows: repeat(2, 1fr);
    padding: 6px 8px 10px;
    column-gap: 18px;
  }
  .pillar { display: flex; flex-direction: column; align-items: center; }
  .pillar-icon { width: 48px; height: 48px; }
  .pillar h2 { font-size: 17px; font-weight: 600; margin: 6px 0 2px; letter-spacing: -.2px; }
  .pillar p {
    font-size: 12.4px; line-height: 16.2px; color: var(--body-text);
    text-align: justify; text-align-last: left; width: 100%;
  }
  .governance h2 { color: var(--governance); }
  .economy h2 { color: var(--economy); }
  .mobility h2 { color: var(--mobility); }
  .environment h2 { color: var(--environment); }
  .people h2 { color: var(--people); }
  .living h2 { color: var(--living); }

  .footer {
    position: absolute; left: 0; top: 1081px; width: 912px; height: 79px;
    background: var(--footer-bg); color: #fff;
  }
  .partner {
    position: absolute; left: 66px; top: 24px;
    display: flex; align-items: center; gap: 12px;
  }
  .partner-dot { width: 30px; height: 30px; border-radius: 50%; background: #fff; }
  .partner-name { font-size: 26px; font-weight: 400; letter-spacing: .5px; }
  .addresses {
    position: absolute; left: 352px; top: 12px;
    font-size: 12.4px; font-weight: 600; line-height: 18.5px;
  }
  .contact-line { display: flex; align-items: flex-start; gap: 10px; }
  .contact-line svg { flex: none; margin-top: 3px; }
  .contact-line .spacer { width: 10px; flex: none; }
  .online {
    position: absolute; left: 702px; top: 16px;
    font-size: 12.4px; font-weight: 600; line-height: 26px;
  }
</style>
</head>
<body>
<main class="flyer">

  <header class="masthead">
    <div class="brand">
      <span class="brand-mark"></span>
      <span class="brand-name">Norvale Group</span>
    </div>
    <div class="call">CALL: 1300 555 019</div>
  </header>

  <div class="hero-photo" role="img" aria-label="Photo of business people at a meeting table, one hand holding a tablet showing bar charts"></div>

  <div class="title-band"><h1>Smart Cities Initiative</h1></div>

  <p class="intro">A smart city is an urban development vision to integrate multiple information and communication technology (ICT) and Internet of things (IoT) solutions in a secure fashion to manage a city's assets – the city's assets include, but are not limited to, local departments' information systems, schools, libraries, transportation systems, hospitals, power plants, water supply networks, waste management, law enforcement, and other community services. The goal of building a smart city is to improve quality of life by using urban informatics and technology to improve the efficiency of services and meet residents' needs. ICT allows city officials to interact directly with the community and the city infrastructure and to monitor what is happening in the city, how the city is evolving, and how to enable a better quality of life. Through the use of sensors integrated with real-time monitoring systems, data are collected from citizens and devices then processed and analyzed. The information and knowledge gathered are keys to tackling inefficiency. Norvale Group has the ability and smarts to push these solutions forward. Norvale Digital and Norvale Group together with the partnership of Corvex and Nimbus Cloud hosting all these systems, solutions and devices have never been easier and cost effective to deploy and capitalize on.</p>

  <section class="pillars">
    <article class="pillar governance">
      <svg class="pillar-icon" viewBox="0 0 48 48" aria-hidden="true">
        <circle cx="24" cy="24" r="22" fill="none" stroke="var(--navy)" stroke-width="3"/>
        <path d="M12 16h18a3 3 0 0 1 3 3v8a3 3 0 0 1-3 3H20l-5 4v-4h-3a3 3 0 0 1-3-3v-8a3 3 0 0 1 3-3z" fill="#bfe6f7" stroke="#1a3f73" stroke-width="1.5"/>
        <circle cx="16" cy="23" r="1.5" fill="#1a3f73"/><circle cx="21" cy="23" r="1.5" fill="#1a3f73"/><circle cx="26" cy="23" r="1.5" fill="#1a3f73"/>
      </svg>
      <h2>SMART GOVERNANCE</h2>
      <p>Interconnected within-city and across-city governance, including ICT-enabled services and interactions between public and private sectors.</p>
    </article>
    <article class="pillar economy">
      <svg class="pillar-icon" viewBox="0 0 48 48" aria-hidden="true">
        <circle cx="24" cy="24" r="22" fill="none" stroke="var(--navy)" stroke-width="3"/>
        <circle cx="24" cy="24" r="10" fill="#fbd3da" stroke="var(--economy)" stroke-width="1.8"/>
        <path d="M14 24h20M24 14v20M17 17c4 3 10 3 14 0M17 31c4-3 10-3 14 0" fill="none" stroke="var(--economy)" stroke-width="1.4"/>
      </svg>
      <h2>SMART ECONOMY</h2>
      <p>E-business and e-commerce, ICT-enabled manufacturing and delivery of services, as well as new products, new services and business models.</p>
    </article>
    <article class="pillar mobility">
      <svg class="pillar-icon" viewBox="0 0 48 48" aria-hidden="true">
        <circle cx="24" cy="24" r="22" fill="none" stroke="var(--navy)" stroke-width="3"/>
        <circle cx="15" cy="28" r="6" fill="none" stroke="#222" stroke-width="1.6"/>
        <circle cx="33" cy="28" r="6" fill="#fbe98a" stroke="#222" stroke-width="1.6"/>
        <path d="M15 28l6-9h9l3 9M21 19l4 9h-10M19 17h5" fill="none" stroke="#222" stroke-width="1.6"/>
      </svg>
      <h2>SMART MOBILITY</h2>
      <p>ICT supported and integrated transport and logistics. Sustainable, safe &amp; interconnected systems for public transport, cars, bicycles and pedestrians.</p>
    </article>
    <article class="pillar environment">
      <svg class="pillar-icon" viewBox="0 0 48 48" aria-hidden="true">
        <circle cx="24" cy="24" r="22" fill="none" stroke="var(--navy)" stroke-width="3"/>
        <circle cx="26" cy="21" r="8" fill="var(--environment)" stroke="#1d5a1a" stroke-width="1.5"/>
        <path d="M26 21v16" stroke="#1d5a1a" stroke-width="2.2"/>
      </svg>
      <h2>SMART ENVIRONMENT</h2>
      <p>Smart energy including renewables, ICT-enabled energy grids, pollution control and monitoring, green buildings and green urban planning.</p>
    </article>
    <article class="pillar people">
      <svg class="pillar-icon" viewBox="0 0 48 48" aria-hidden="true">
        <circle cx="24" cy="24" r="22" fill="none" stroke="var(--navy)" stroke-width="3"/>
        <path d="M24 14a8 8 0 0 1 5 14v4h-10v-4a8 8 0 0 1 5-14z" fill="#f3c58f" stroke="#333" stroke-width="1.5"/>
        <path d="M20 35h8" stroke="#333" stroke-width="1.8"/>
        <path d="M24 8v3M14 12l2 2M34 12l-2 2" stroke="#333" stroke-width="1.5"/>
      </svg>
      <h2>SMART PEOPLE</h2>
      <p>Those with e-skills, working in ICT-enabled roles, having access to education and training, human resources and capacity management.</p>
    </article>
    <article class="pillar living">
      <svg class="pillar-icon" viewBox="0 0 48 48" aria-hidden="true">
        <circle cx="24" cy="24" r="22" fill="none" stroke="var(--navy)" stroke-width="3"/>
        <circle cx="17" cy="31" r="2.5" fill="var(--living)"/>
        <path d="M17 23a8 8 0 0 1 8 8M17 16a15 15 0 0 1 15 15" fill="none" stroke="var(--living)" stroke-width="3" stroke-linecap="round"/>
      </svg>
      <h2>SMART LIVING</h2>
      <p>ICT-enabled lifestyles, behaviour and consumption. Healthy and safe living in a culturally vibrant city with good quality housing.</p>
    </article>
  </section>

  <footer class="footer">
    <div class="partner">
      <span class="partner-dot"></span>
      <span class="partner-name">Corvex PARTNER</span>
    </div>
    <div class="addresses">
      <div class="contact-line">
        <svg width="11" height="14" viewBox="0 0 11 14" aria-hidden="true"><path d="M5.5 0a5.5 5.5 0 0 1 5.5 5.5C11 9 5.5 14 5.5 14S0 9 0 5.5A5.5 5.5 0 0 1 5.5 0z" fill="#fff"/><circle cx="5.5" cy="5.3" r="2" fill="#1c1c1e"/></svg>
        <span>Head Office 118-120 Harlow Road<br>Kensley, NSW, 2210</span>
      </div>
      <div class="contact-line">
        <svg width="11" height="14" viewBox="0 0 11 14" aria-hidden="true"><path d="M5.5 0a5.5 5.5 0 0 1 5.5 5.5C11 9 5.5 14 5.5 14S0 9 0 5.5A5.5 5.5 0 0 1 5.5 0z" fill="#fff"/><circle cx="5.5" cy="5.3" r="2" fill="#1c1c1e"/></svg>
        <span>14 Ashby Lane Sydney NSW 2000</span>
      </div>
    </div>
    <div class="online">
      <div class="contact-line">
        <svg width="17" height="14" viewBox="0 0 17 14" aria-hidden="true" style="margin-top:6px"><rect x="1" y="1" width="15" height="9" fill="none" stroke="#fff" stroke-width="1.3"/><path d="M6 13h5M8.5 10v3" stroke="#fff" stroke-width="1.3"/></svg>
        <span>info@norvalegroup.com.au</span>
      </div>
      <div class="contact-line">
        <svg width="17" height="14" viewBox="0 0 17 14" aria-hidden="true" style="margin-top:6px"><rect x="1" y="1.5" width="15" height="11" fill="none" stroke="#fff" stroke-width="1.3"/><path d="M1 1.5l7.5 6 7.5-6" fill="none" stroke="#fff" stroke-width="1.3"/></svg>
        <span>www.norvalegroup.com.au</span>
      </div>
    </div>
  </footer>

</main>
</body>
</html>
```